Business Card design for an International Import Export House

We need a Business Card design for our import export business. We trade in Minerals, Metals, Rice, Sugar, Steel etc.. The design should be minimalistic. It may or may not contain the physical address. In case you want to include the physical address - 418 Marwick Plaza, Oakvale Sector 7, Northfield, Kestria, Avalon, 560118.

Target Market(s)

Steel Mills or Steel Plants, Factories, Mining businesses, Industrial houses, Government Agencies

Industry/Entity Type

Importer

Contact Information for Business Card

Business Name - Verrano Trade

Font styles to use
Other font styles liked:
• montserrat

Requirements
Must have
• Darin Pohlak - President
• www.verranotrade.example
• darin@verranotrade.example
• +91-988-412-3675
Nice to have
• worldwide suppliers of ores

```html
<!DOCTYPE html>
<html lang="en">
<head>
<meta charset="utf-8">
<title>Verrano Trade — Business Card</title>
<link rel="stylesheet" href="https://fonts.googleapis.com/css2?family=Montserrat:wght@700&family=Source+Sans+3:wght@400;600&display=swap">
<style>
  :root {
    --teal: #2f8fa9;
    --teal-dark: #26788f;
    --ink: #1d1d1f;
    --paper: #ffffff;
    --rule: #8fb9c6;
    --stage: #e7e9ea;
  }
  * { box-sizing: border-box; margin: 0; padding: 0; }
  html, body { width: 1200px; height: 912px; overflow: hidden; }
  body {
    background: var(--stage);
    position: relative;
    font-family: "Source Sans 3", "Myriad Pro", sans-serif;
    color: var(--ink);
  }
  .card {
    position: absolute;
    width: 560px;
    height: 320px;
    box-shadow: 0 6px 18px rgba(0,0,0,.18);
    overflow: hidden;
  }

  /* Front side */
  .card-front {
    left: 80px; top: 90px;
    background: var(--teal);
    display: flex;
    flex-direction: column;
    align-items: center;
  }
  .front-brand {
    margin-top: 70px;
    display: flex;
    flex-direction: column;
    align-items: center;
    gap: 18px;
  }
  .brand-dot {
    width: 74px; height: 74px;
    border-radius: 50%;
    background: var(--paper);
  }
  .front-brand .brand-name {
    font-family: "Montserrat", sans-serif;
    font-weight: 700;
    font-size: 27px;
    letter-spacing: -0.5px;
    color: var(--paper);
    text-transform: uppercase;
  }
  .front-url {
    position: absolute;
    bottom: 34px;
    font-size: 19px;
    letter-spacing: 3px;
    color: var(--ink);
  }

  /* Back side */
  .card-back {
    left: 560px; top: 500px;
    background: var(--paper) repeating-linear-gradient(180deg, transparent 0 4px, rgba(0,0,0,.035) 4px 5px);
  }
  .back-band {
    position: absolute;
    left: 0; right: 0; bottom: 0;
    height: 26px;
    background: var(--teal);
    border-top: 3px solid var(--ink);
  }
  .back-brand {
    position: absolute;
    left: 40px; top: 70px;
    width: 210px;
    display: flex;
    flex-direction: column;
    align-items: center;
    gap: 16px;
  }
  .back-brand .brand-dot { background: var(--teal); width: 70px; height: 70px; }
  .back-brand .brand-name {
    font-family: "Montserrat", sans-serif;
    font-weight: 700;
    font-size: 22px;
    letter-spacing: -0.5px;
    color: var(--teal);
    text-transform: uppercase;
  }
  .divider {
    position: absolute;
    left: 278px; top: 40px;
    width: 1px; height: 214px;
    background: var(--rule);
  }
  .contact {
    position: absolute;
    left: 300px; top: 38px;
    font-size: 14.5px;
    line-height: 1.3;
  }
  .contact .person {
    font-weight: 600;
    font-size: 20px;
    color: var(--teal);
  }
  .contact .role { font-size: 16px; margin-bottom: 8px; }
  .contact address { font-style: normal; margin-bottom: 8px; }
  .contact ul { list-style: none; }
  .contact li { display: flex; align-items: center; gap: 6px; margin-bottom: 3px; }
  .icon {
    width: 17px; height: 17px;
    border-radius: 50%;
    background: var(--teal);
    display: inline-flex;
    align-items: center;
    justify-content: center;
    flex: none;
  }
  .icon svg { width: 11px; height: 11px; }
</style>
</head>
<body>

<section class="card card-front">
  <div class="front-brand">
    <span class="brand-dot"></span>
    <span class="brand-name">Verrano Trade</span>
  </div>
  <p class="front-url">www.verranotrade.example</p>
</section>

<section class="card card-back">
  <div class="back-brand">
    <span class="brand-dot"></span>
    <span class="brand-name">Verrano Trade</span>
  </div>
  <span class="divider"></span>
  <div class="contact">
    <p class="person">Darin Pohlak</p>
    <p class="role">President</p>
    <address>418 Marwick Plaza,<br>Oakvale Sector 7, Northfield,<br>Kestria, Avalon, 560118.</address>
    <ul>
      <li><span class="icon"><svg viewBox="0 0 12 12"><rect x="3.5" y="1" width="5" height="10" rx="1" fill="none" stroke="#fff" stroke-width="1.2"/></svg></span>+91-988-412-3675</li>
      <li><span class="icon"><svg viewBox="0 0 12 12"><rect x="1" y="3" width="10" height="6.5" fill="none" stroke="#fff" stroke-width="1.2"/><path d="M1 3l5 4 5-4" fill="none" stroke="#fff" stroke-width="1.2"/></svg></span>darin@verranotrade.example</li>
      <li><span class="icon"><svg viewBox="0 0 12 12"><circle cx="6" cy="6" r="4.6" fill="none" stroke="#fff" stroke-width="1.1"/><ellipse cx="6" cy="6" rx="2" ry="4.6" fill="none" stroke="#fff" stroke-width="1"/><path d="M1.4 6h9.2" stroke="#fff" stroke-width="1"/></svg></span>www.verranotrade.example</li>
    </ul>
  </div>
  <div class="back-band"></div>
</section>

</body>
</html>
```